Redesign of a Restaurant web presence

We need a new design of our restaurant web page which can also be based on a new CI (current main colours are gold, green and pink/violett), urban jungle style.
WORDPRESS is being used for coding the website and there should be no monthly paid plug-ins be used.
Main features should be the presentation of our location, downloadable menus (pdf), a possibility for online reservations (pop-up on start page) and recruitung staff (job descriptions to be viewed).
Focus should be on the design, functionality is very basic.
Multi language preferred (SK,DE,EN).
Working on desktop and mobile devices.
A reference site is fernloft.at
Current page tovimarlund.sk
If the co-operation is good, we also need template layouts for our new printed menu based on the (new) CI.

```html
<!DOCTYPE html>
<html lang="en">
<head>
<meta charset="utf-8">
<title>Marlund Kitchen – Café &amp; Restaurant</title>
<link rel="stylesheet" href="https://fonts.googleapis.com/css2?family=Cinzel:wght@400;500;600&family=Dancing+Script:wght@600;700&family=Open+Sans:wght@400;600&display=swap">
<style>
:root{
  --gold:#d4b12f;
  --ink:#1e1e1e;
  --white:#fff;
  --sky:#d9f0f3;
  --cream:#f8f0c0;
  --pink:#fbdff0;
  --mint:#d1f5c0;
  --pale-blue:#dff1f6;
  --paper:#f1f0ee;
  --events:#faf1c3;
  --black:#0b0b0b;
  --field:#eeeeee;
}
*{box-sizing:border-box;margin:0;padding:0}
html,body{width:1200px;height:4402px;overflow:hidden;background:var(--white)}
body{font-family:"Open Sans",Arial,sans-serif;color:var(--ink)}
.page{position:relative;width:1200px;height:4402px;overflow:hidden}
.abs{position:absolute}
.serif{font-family:"Cinzel",Georgia,serif}
.script{font-family:"Dancing Script",cursive;color:var(--gold);font-weight:700}
.center{left:0;width:1200px;text-align:center}
.vline{position:absolute;left:599px;width:1px;background:#555}
.nowrap{white-space:nowrap}

.topbar{top:0;left:0;width:1200px;height:26px;background:var(--gold);color:var(--white);font-size:10px;font-family:"Cinzel",serif}
.topbar span{position:absolute;top:7px;white-space:nowrap}
.dot{position:absolute;top:5px;width:16px;height:16px;border:1.5px solid var(--ink);border-radius:50%}

.nav{top:26px;left:0;width:1200px;height:66px;background:var(--white)}
.nav a{position:absolute;top:28px;font-family:"Cinzel",serif;font-size:11px;color:var(--ink);text-decoration:none;font-weight:600;white-space:nowrap}
.nav a.active{color:var(--gold);border-bottom:1px solid var(--gold)}
.brand{position:absolute;text-align:center;font-family:"Cinzel",serif;color:var(--ink);white-space:nowrap}
.brand .name{font-size:19px;letter-spacing:1px;line-height:1}
.brand .sub{font-size:9px;letter-spacing:2px;margin-top:5px;border-top:1px solid var(--ink);padding-top:3px}
.lang{position:absolute;left:991px;top:24px;width:46px;height:20px;background:var(--gold);color:var(--white);font-size:9px;text-align:center;line-height:20px;font-family:"Cinzel",serif}

.hero{top:92px;left:0;width:1200px;height:494px;background:linear-gradient(120deg,#1f6f7a 0%,#2a8c98 30%,#7b5a3a 55%,#2b9aa6 75%,#c89b62 100%)}
.hero-shade{top:92px;left:0;width:1200px;height:494px;background:rgba(0,0,0,.28)}
.btn{position:absolute;background:var(--gold);color:var(--white);font-family:"Cinzel",serif;font-size:11px;text-align:center;white-space:nowrap}

.leaf{background:linear-gradient(160deg,#1b8f5a,#57c28a 45%,#e9679d 70%,#2a9c6a)}
.card{left:318px;top:788px;width:562px;height:460px;background:var(--white);box-shadow:0 0 10px rgba(0,0,0,.15)}
.card-inner{left:334px;top:803px;width:530px;height:430px;border:1px solid #999}
.field{position:absolute;height:30px;background:var(--field);font-family:"Cinzel",serif;font-size:9px;color:#666;padding:9px 14px;white-space:nowrap}

.row{position:absolute;height:66px;font-family:"Cinzel",serif;font-size:21px;letter-spacing:1px;color:var(--ink)}
.row span{position:absolute;top:20px;white-space:nowrap}
.photo{position:absolute;border:3px solid var(--white);box-shadow:0 2px 6px rgba(0,0,0,.25)}
.tri{position:absolute;width:0;height:0;border-left:10px solid transparent;border-right:10px solid transparent;border-top:10px solid var(--ink)}

.about p{font-size:11px;line-height:19px;color:#444}

.spec{position:absolute;top:2757px;height:294px}
.spec span{position:absolute;bottom:16px;left:0;width:100%;text-align:center;font-family:"Cinzel",serif;font-size:22px;color:var(--white);text-shadow:0 1px 4px rgba(0,0,0,.6);white-space:nowrap}

.footer{top:4188px;left:0;width:1200px;height:214px;background:var(--black);color:var(--white);z-index:1}
.subscribe-wrap{position:absolute;left:0;top:0;width:1200px;height:4402px;z-index:2;pointer-events:none}
.subscribe{left:159px;top:4096px;width:875px;height:123px;background:var(--gold);border-radius:16px}
</style>
</head>
<body>
<div class="page">

  <div class="abs topbar">
    <svg class="abs" style="left:160px;top:7px" width="11" height="11" viewBox="0 0 24 24"><path fill="#fff" d="M6.6 10.8a15 15 0 0 0 6.6 6.6l2.2-2.2a1 1 0 0 1 1-.25 11.4 11.4 0 0 0 3.6.57 1 1 0 0 1 1 1V20a1 1 0 0 1-1 1A17 17 0 0 1 3 4a1 1 0 0 1 1-1h3.5a1 1 0 0 1 1 1c0 1.250.2 2.450.57 3.6a1 1 0 0 1-.25 1z"/></svg>
    <span style="left:178px">+421 900 314 275</span>
    <svg class="abs" style="left:298px;top:8px" width="12" height="9" viewBox="0 0 24 18"><rect x="1" y="1" width="22" height="16" fill="none" stroke="#fff" stroke-width="2"/><path d="M1 1l11 9 11-9" fill="none" stroke="#fff" stroke-width="2"/></svg>
    <span style="left:316px">info@tovimarlund.sk</span>
    <div class="dot" style="left:994px"></div>
    <div class="dot" style="left:1016px"></div>
  </div>

  <nav class="abs nav">
    <a class="active" style="left:161px">Introduction</a>
    <a style="left:282px">Daily menu</a>
    <a style="left:389px">Our offer</a>
    <div class="brand" style="left:508px;top:14px;width:184px">
      <div class="name">MARLUND KITCHEN</div>
      <div class="sub">CAFÉ &amp; RESTAURANT</div>
    </div>
    <a style="left:717px">Events</a>
    <a style="left:792px">Reservation</a>
    <a style="left:900px">Contacts</a>
    <div class="lang">ENG ▾</div>
  </nav>

  <div class="abs hero" role="img" aria-label="Photo of the restaurant interior with teal velvet seating, wooden tables and a bar"></div>
  <div class="abs hero-shade"></div>
  <div class="abs center script" style="top:208px;font-size:54px;color:var(--white)">Welcome To</div>
  <div class="abs center serif" style="top:272px;font-size:42px;line-height:36px;color:var(--white)">We bring the experience<br>of food and a great<br>atmosphere</div>
  <div class="abs" style="left:372px;top:386px;width:456px;height:1px;background:var(--white)"></div>
  <div class="btn" style="left:528px;top:415px;width:145px;height:32px;line-height:32px">JOIN THE TEAM</div>
  <div class="abs" style="left:570px;top:476px;width:28px;height:28px;border-radius:50%;background:var(--white)"></div>
  <svg class="abs" style="left:577px;top:483px" width="14" height="14" viewBox="0 0 14 14"><path d="M12 7H2M6 3L2 7l4 4" fill="none" stroke="#222" stroke-width="1.6"/></svg>
  <svg class="abs" style="left:611px;top:483px" width="14" height="14" viewBox="0 0 14 14"><path d="M2 7h10M8 3l4 4-4 4" fill="none" stroke="#fff" stroke-width="1.2" opacity=".7"/></svg>

  <div class="vline" style="top:586px;height:64px"></div>
  <div class="abs leaf" style="left:0;top:586px;width:220px;height:747px;clip-path:polygon(0 0,100% 8%,60% 30%,95% 55%,50% 80%,70% 100%,0 100%)" role="img" aria-label="Illustration of tropical palm leaves and pink flowers"></div>
  <div class="abs leaf" style="left:980px;top:586px;width:220px;height:747px;clip-path:polygon(100% 0,0 8%,40% 30%,5% 55%,50% 80%,30% 100%,100% 100%)" role="img" aria-label="Illustration of tropical palm leaves and pink flowers"></div>
  <div class="abs center script" style="top:678px;font-size:38px">Marlund Kitchen</div>
  <div class="abs center serif" style="top:726px;font-size:26px">Book a pleasant experience with us</div>
  <div class="abs card"></div>
  <div class="abs card-inner"></div>
  <svg class="abs" style="left:582px;top:820px" width="36" height="36" viewBox="0 0 36 36"><path d="M4 4l28 28M32 4L4 32" stroke="#222" stroke-width="2"/><path d="M4 4c6 0 10 4 10 10" fill="none" stroke="#222" stroke-width="2"/><path d="M26 2l8 8" stroke="#222" stroke-width="2"/></svg>
  <div class="field" style="left:369px;top:866px;width:226px">FULL NAME</div>
  <div class="field" style="left:605px;top:866px;width:227px">DATE OF RESERVATION</div>
  <div class="field" style="left:369px;top:908px;width:226px">EMAIL</div>
  <div class="field" style="left:605px;top:908px;width:227px">TIME OF ARRIVAL</div>
  <div class="field" style="left:369px;top:950px;width:226px">PHONE</div>
  <div class="field" style="left:605px;top:950px;width:227px">NUMBER OF PEOPLE</div>
  <div class="field" style="left:369px;top:994px;width:463px;height:106px">MESSAGE</div>
  <div class="abs nowrap" style="left:369px;top:1112px;font-size:9px;color:#555">Complete the requirements according to your wishes for an experience in Marlund Kitchen</div>
  <div class="btn" style="left:526px;top:1141px;width:148px;height:32px;line-height:32px">TO SEND</div>
  <div class="abs" style="left:369px;top:1187px;width:13px;height:13px;border:1px solid #888"></div>
  <div class="abs nowrap" style="left:389px;top:1188px;font-size:9px;color:#555">Consent to the processing of personal data</div>

  <div class="abs" style="left:0;top:1333px;width:1200px;height:645px;background:var(--sky)"></div>
  <div class="vline" style="top:1303px;height:102px"></div>
  <div class="abs center serif" style="top:1420px;font-size:40px">Our offer</div>

  <div class="row" style="left:237px;top:1526px;width:726px;background:var(--cream)"><span style="left:380px">Menu</span></div>
  <div class="photo" style="left:297px;top:1505px;width:163px;height:102px;background:linear-gradient(135deg,#6b8f3a,#c9a46a,#3f5e2a)" role="img" aria-label="Photo of a fresh salad plate"></div>
  <div class="tri" style="left:892px;top:1555px"></div>

  <div class="row" style="left:237px;top:1627px;width:726px;background:var(--pink)"><span style="left:212px">Drink menu</span></div>
  <div class="photo" style="left:744px;top:1607px;width:162px;height:102px;background:linear-gradient(135deg,#3a2a22,#7a1f2a,#b9905e)" role="img" aria-label="Photo of two glasses of red wine being toasted"></div>
  <div class="tri" style="left:292px;top:1656px"></div>

  <div class="row" style="left:233px;top:1730px;width:725px;background:var(--cream)"><span style="left:362px">Wine list</span></div>
  <div class="photo" style="left:297px;top:1710px;width:163px;height:102px;background:linear-gradient(135deg,#e8e8e8,#cfcfcf 55%,#8a1a22)" role="img" aria-label="Photo of red wine being poured into a glass"></div>
  <div class="tri" style="left:886px;top:1759px"></div>

  <div class="row" style="left:237px;top:1833px;width:726px;background:var(--mint)"><span style="left:202px">Chef's special</span></div>
  <div class="photo" style="left:744px;top:1812px;width:162px;height:100px;background:linear-gradient(135deg,#2e3430,#6d7468,#c9c0b0)" role="img" aria-label="Photo of a chef plating a dish"></div>
  <div class="tri" style="left:292px;top:1862px"></div>

  <div class="abs" style="left:0;top:1978px;width:1200px;height:617px;background:var(--paper)"></div>
  <div class="abs" style="left:98px;top:2065px;width:250px;height:1px;background:#999"></div>
  <div class="abs" style="left:98px;top:2065px;width:1px;height:410px;background:#999"></div>
  <div class="abs" style="left:108px;top:2078px;width:432px;height:383px;background:linear-gradient(135deg,#d49a2c,#c58a22 45%,#f0efe8 60%,#b5227a)" role="img" aria-label="Photo of a dining room with golden walls and pink chairs"></div>
  <div class="abs" style="left:373px;top:2302px;width:225px;height:217px;border:4px solid var(--white);box-shadow:0 2px 8px rgba(0,0,0,.3);background:linear-gradient(135deg,#bdbdbd,#e6e2da 50%,#3b3b3b)" role="img" aria-label="Photo of the restaurant owner standing by a laid table"></div>
  <div class="abs" style="left:1040px;top:2290px;width:160px;height:305px;background:linear-gradient(180deg,#e0e0e0,#9c9c9c)" role="img" aria-label="Decorative grey ostrich figure on a white wall"></div>

  <div class="abs script" style="left:672px;top:2098px;font-size:34px">Welcome To</div>
  <div class="abs serif nowrap" style="left:672px;top:2134px;font-size:32px">Marlund Kitchen</div>
  <div class="abs about" style="left:672px;top:2183px;width:365px">
    <p>Our restaurant combines modern cuisine with elements of tradition, home Slovak specialties with delicious gastronomic experiences from other countries. We create the concept and alchemy of Marlund Kitchen sensitively and interactively based on many years of foreign experience and rich practice. We hold fast to our values, such as quality, freshness, locality, seasonality.</p>
    <p style="margin-top:11px">We maintain a high level of our work and try to move one step forward every day. Choosing a meal can be a challenge, an experience, and an adventure for you at Marlund Kitchen, because every meal is a win with us. You will find us in a quiet and pleasant location in Brezová Lúka. Come and have a pleasant time for your body and soul. We invite you.</p>
  </div>
  <div class="abs" style="left:675px;top:2445px;width:75px;height:1px;background:#777"></div>
  <div class="abs serif nowrap" style="left:765px;top:2427px;font-size:16px;color:var(--gold)">Mira Dolanová</div>
  <div class="abs nowrap" style="left:761px;top:2450px;font-size:11px;color:#333">Owner of the Restaurant</div>

  <div class="vline" style="top:2570px;height:90px"></div>
  <div class="abs center serif" style="top:2676px;font-size:38px">Our specialties</div>
  <div class="spec" style="left:0;width:385px;background:radial-gradient(circle at 50% 45%,#4a2a1a 0,#3a2518 30%,#d8d2c8 55%,#2b3236 80%)" role="img" aria-label="Photo of a chocolate lava cake with vanilla sauce"><span>Chocolate lava cake</span></div>
  <div class="spec" style="left:402px;width:396px;background:radial-gradient(circle at 50% 50%,#e8b93a 0,#d89f2e 25%,#1f3a36 45%,#d9d6d2 70%)" role="img" aria-label="Photo of a bowl of Tom Kha Gai soup"><span>Tom Kha Gai soup</span></div>
  <div class="spec" style="left:815px;width:385px;background:radial-gradient(circle at 50% 45%,#b8702e 0,#9a5a24 30%,#dedbd5 60%,#b9b5ae)" role="img" aria-label="Photo of a pulled pork burger"><span>Pulled pork burger</span></div>

  <div class="abs" style="left:0;top:3051px;width:1200px;height:458px;background:var(--events)"></div>
  <div class="abs" style="left:0;top:3180px;width:1200px;height:329px;background:linear-gradient(180deg,rgba(171,196,150,0) 0%,rgba(171,196,150,.35) 100%)" role="img" aria-label="Faint illustration of large green tropical leaves"></div>
  <div class="abs center serif" style="top:3128px;font-size:40px">Events</div>

  <div class="row" style="left:237px;top:3237px;width:726px;background:var(--mint)"><span style="left:308px">Tailor-made events</span></div>
  <div class="photo" style="left:297px;top:3217px;width:163px;height:103px;background:linear-gradient(135deg,#6e5a44,#c49a7a,#3a4a2e)" role="img" aria-label="Photo of joined hands at a wedding"></div>
  <div class="tri" style="left:892px;top:3266px"></div>

  <div class="row" style="left:237px;top:3347px;width:726px;background:var(--pale-blue)"><span style="left:150px">Events for the public</span></div>
  <div class="photo" style="left:744px;top:3326px;width:162px;height:102px;background:linear-gradient(135deg,#3b3a6e,#c4508a,#e9b24a)" role="img" aria-label="Photo of guests celebrating at a party"></div>
  <div class="tri" style="left:292px;top:3376px"></div>

  <div class="abs center script" style="top:3564px;font-size:38px">Tip for a trip</div>
  <div class="abs center serif" style="top:3608px;font-size:30px;line-height:32px;font-weight:500">Discover the beauty of Brezová<br>Lúka</div>
  <div class="abs center" style="top:3690px;font-size:11px;line-height:18px;color:#444">On your walks in Brezová Lúka and its surroundings, you will certainly be attracted by its diversity,<br>natural and cultural wealth. We recommend visiting these places and ways to make yourself or your family<br>a pleasant experience.</div>

  <div class="abs" style="left:0;top:3798px;width:1200px;height:390px;background:linear-gradient(120deg,#d6ece6 0%,#eef0ec 30%,#f3f3f1 60%,#e4ece2 100%)" role="img" aria-label="Street map of the neighbourhood showing the restaurant location"></div>
  <svg class="abs" style="left:525px;top:3976px" width="16" height="22" viewBox="0 0 16 22"><path d="M8 0a8 8 0 0 1 8 8c0 6-8 14-8 14S0 14 0 8a8 8 0 0 1 8-8z" fill="#e53935"/><circle cx="8" cy="8" r="3" fill="#fff"/></svg>

  <footer class="abs footer">
    <div class="brand" style="left:160px;top:80px;width:230px;color:var(--white)">
      <div class="name" style="font-size:23px">MARLUND KITCHEN</div>
      <div class="sub" style="border-color:var(--white);font-size:10px">CAFÉ &amp; RESTAURANT</div>
    </div>
    <div class="abs serif nowrap" style="left:498px;top:80px;font-size:18px">Lipová 1184/12</div>
    <div class="abs nowrap" style="left:498px;top:108px;font-size:10px;line-height:17px;font-weight:600">962 15 Lomnica<br>Brezová Lúka</div>
    <div class="abs serif nowrap" style="left:728px;top:80px;font-size:16px">info@tovimarlund.sk</div>
    <div class="abs nowrap" style="left:728px;top:108px;font-size:10px;font-weight:600">+421 900 314 275</div>
    <div class="abs" style="left:973px;top:86px;width:28px;height:28px;border:2px solid var(--white);border-radius:50%"></div>
    <div class="abs" style="left:1008px;top:86px;width:28px;height:28px;border:2px solid var(--white);border-radius:50%"></div>
    <div class="abs" style="left:160px;top:190px;width:880px;height:1px;background:#444"></div>
    <div class="abs center" style="top:198px;font-size:9px;font-weight:600">Copyright © 2024 Marlund Kitchen. All rights reserved.</div>
  </footer>

  <div class="subscribe-wrap">
    <div class="abs subscribe"></div>
    <div class="abs serif nowrap" style="left:220px;top:4143px;font-size:24px;color:var(--ink)">Subscribe to our news</div>
    <div class="abs nowrap" style="left:577px;top:4131px;width:248px;height:36px;border-bottom:1px solid var(--white);font-size:9px;color:var(--white);padding:13px 12px">Enter your email</div>
    <div class="abs serif" style="left:839px;top:4131px;width:126px;height:36px;background:var(--white);font-size:10px;font-weight:600;text-align:center;line-height:36px">SUBSCRIBE</div>
    <div class="abs" style="left:577px;top:4180px;width:13px;height:13px;background:var(--white)"></div>
    <div class="abs nowrap" style="left:597px;top:4181px;font-size:8px;color:var(--white)">I agree to the processing of personal data</div>
    <div class="abs" style="left:785px;top:4180px;width:13px;height:13px;background:var(--white)"></div>
    <div class="abs nowrap" style="left:806px;top:4181px;font-size:8px;color:var(--white)">I agree with sending the newsletter</div>
  </div>

</div>
</body>
</html>
```